Traffic product supplier - Temporary Raised Pavement Markers

We need a flyer design that will grab the customer's eye to the product (TRPMs) and entice curiosity to the business. Showing 1 product but promoting other products. The following information should be included:
- Logo (attached)
- Sale Product image (Temporary Road Pavement Marker AKA Tack and Treads)
- Product wording (attached word document)

Happy for you to add/amend wording for grammatical purpose and other images that show it is a sale flyer.

Background on KRV - We are a thermoplastic manufacturer for road markings and traffic product supplier. KRV specializes in producing high quality hotmelt thermoplastic that meet Australian Standard AS7312.4. We are able to produce other specifications as required by the customer.

Would like the colour scheme to be similar to the logo.

If you need more information let me know.

Target Market(s)

Asphalt industry / road builders

Font styles to use
Serif
Sans Serif

Requirements
Must have
• - Kestrel Roadline Ventures (My company name)
- Contact details:
- 02 9471 2385
- marcus.t@krvsupply.com.au
- info@krvsupply.com.au
-www.krvlane.com

- Attached images.
-Title (Temporary Road Pavement Markers)

```html
<!DOCTYPE html>
<html lang="en">
<head>
<meta charset="utf-8">
<title>KRV Temporary Road Pavement Markers Flyer</title>
<link href="https://fonts.googleapis.com/css2?family=Montserrat:wght@400;500;700;800&family=Roboto:wght@400;500&family=Roboto+Condensed:ital,wght@1,500&display=swap" rel="stylesheet">
<style>
:root{
  --blue:#2460a7;
  --blue-deep:#1c58a6;
  --yellow:#f6c812;
  --ink:#2b2b2b;
  --white:#ffffff;
  --grey-bar:#ececec;
  --frame:#cfcfcf;
  --sky:#bcd8ee;
  --road:#5c6167;
}
*{box-sizing:border-box;margin:0;padding:0}
html,body{width:882px;height:1200px;overflow:hidden;background:#f2f2f2}
body{font-family:'Montserrat',sans-serif;color:var(--ink)}
.flyer{position:relative;width:882px;height:1200px;background:var(--white);overflow:hidden}

.hero-photo{position:absolute;left:0;top:0;width:882px;height:478px;
  background:linear-gradient(180deg,#9ec6e8 0%,#dceaf4 34%,#8fae6a 40%,#6f8f4d 44%,#7a7f86 47%,var(--road) 100%)}
.hero-curve{position:absolute;left:0;top:420px;width:882px;height:62px}

.brand{position:absolute;left:97px;top:39px;width:192px;height:119px;display:flex;align-items:center;justify-content:center;gap:12px}
.brand-mark{width:26px;height:26px;background:var(--blue)}
.brand-name{font-family:'Montserrat',sans-serif;font-weight:800;font-size:58px;color:var(--blue);letter-spacing:2px}
.tagline{position:absolute;left:70px;top:168px;font-family:'Roboto Condensed',sans-serif;font-style:italic;font-weight:500;font-size:12.5px;color:var(--blue-deep)}

.product-photo{position:absolute;left:488px;top:380px;width:345px;height:232px;border-radius:4px;
  background:linear-gradient(120deg,#f2b90f 0%,#e9a90a 45%,#e6e6e6 55%,#f4f4f4 100%)}

.title{position:absolute;left:68px;top:508px;font-weight:800;font-size:36px;line-height:41px;color:var(--blue-deep);letter-spacing:.3px}
.title-rule{position:absolute;left:72px;top:601px;width:730px;height:4px;background:var(--blue)}
.title-rule::before{content:"";position:absolute;left:0;top:0;width:88px;height:4px;background:var(--yellow)}

.intro{position:absolute;left:70px;top:624px;width:740px;font-size:14.2px;line-height:21.5px}
.intro strong{font-weight:700}

.details{position:absolute;left:72px;top:724px;width:380px;font-size:14.2px;line-height:19.5px}
.details p+p{margin-top:10px}
.details .hl{color:var(--blue-deep);font-weight:700}

.price{position:absolute;left:74px;top:930px;display:flex;align-items:center;gap:6px}
.price-tag{background:var(--yellow);color:var(--blue-deep);font-weight:700;font-size:20px;padding:2px 5px;line-height:24px}
.price-slash{width:3px;height:28px;background:var(--blue-deep);transform:skewX(-14deg)}
.price-note{font-family:'Roboto',sans-serif;font-size:17px;color:var(--blue-deep)}

.dims-head{position:absolute;left:498px;top:725px;display:flex;align-items:stretch}
.dims-head span{background:var(--yellow);color:var(--blue-deep);font-weight:700;font-size:17px;padding:3px 8px 3px 6px}
.dims-head i{display:block;width:3px;margin-left:4px;background:var(--blue-deep);transform:skewX(-14deg)}
.dims{position:absolute;left:498px;top:759px;width:304px;height:216px;background:var(--blue);padding:16px 12px 0 44px;list-style:none;color:var(--white)}
.dims::before{content:"";position:absolute;left:24px;top:24px;width:2px;height:148px;background:var(--yellow)}
.dims li{position:relative;font-weight:500;font-size:14.2px;line-height:19px;margin-bottom:7px}
.dims li::before{content:"";position:absolute;left:-26px;top:3px;width:9px;height:9px;border-radius:50%;background:var(--yellow);border:1px solid var(--yellow)}

.range{position:absolute;left:75px;top:1000px;display:flex;gap:10px}
.range-item{width:175px;height:90px;border:1px solid var(--frame);padding:8px}
.range-item div{width:100%;height:100%}
.r1{background:linear-gradient(90deg,#e9441e 0 33%,#1f3f7a 33% 66%,#f3c11a 66%)}
.r2{background:linear-gradient(100deg,#d9d9d9 0%,#b89045 50%,#e2e2e2 100%)}
.r3{background:linear-gradient(90deg,#c9a874 0%,#2b2b2b 45%,#3a3a3a 100%)}
.r4{background:linear-gradient(90deg,#e3a124 0 48%,#fff 48% 52%,#5b8a5e 52%)}

.call{position:absolute;left:0;top:1111px;width:325px;height:89px}
.call-text{position:absolute;left:0;top:1122px;width:297px;text-align:center;color:var(--white)}
.call-text .lead{font-size:23px;font-weight:400;letter-spacing:1px;line-height:26px}
.call-text .phone{font-size:28px;font-weight:800;letter-spacing:.5px;line-height:34px}

.company{position:absolute;left:352px;top:1132px;font-weight:700;font-size:15.5px;color:var(--blue-deep)}
.web{position:absolute;left:665px;top:1128px;width:139px;height:26px;background:var(--blue);color:var(--white);font-weight:700;font-size:13.5px;border-radius:5px 5px 0 0;display:flex;align-items:center;justify-content:center}
.contact-bar{position:absolute;left:332px;top:1155px;width:550px;height:26px;background:var(--grey-bar);display:flex;align-items:center;gap:18px;padding-left:36px;font-size:13px}
.contact-bar span{display:flex;align-items:center;gap:7px}
</style>
</head>
<body>
<main class="flyer">
  <div class="hero-photo" role="img" aria-label="Photo of a freshly laid asphalt road with double yellow centre lines, roadside gardens and city towers under a blue sky"></div>
  <svg class="hero-curve" viewBox="0 0 882 62" preserveAspectRatio="none" aria-hidden="true">
    <path d="M0 58 L370 58 C410 58 425 42 440 22 C452 8 460 2 480 2 L882 2 L882 62 L0 62 Z" fill="#2460a7"/>
    <path d="M0 60 L380 60 C420 60 432 44 447 24 C459 10 468 4 488 4 L882 4 L882 62 L0 62 Z" fill="#f6c812"/>
    <path d="M0 62 L395 62 C430 62 442 46 456 26 C468 12 476 6 496 6 L882 6 L882 62 Z" fill="#ffffff"/>
  </svg>

  <div class="brand"><span class="brand-mark"></span><span class="brand-name">KRV</span></div>
  <p class="tagline">“Creating a Safe Environment for All Road Users”</p>

  <div class="product-photo" role="img" aria-label="Product photo of a yellow and a white temporary road pavement marker with reflective strips"></div>

  <h1 class="title">TEMPORARY ROAD<br>PAVEMENT MARKERS</h1>
  <div class="title-rule"></div>

  <p class="intro">Temporary road pavement markers, also known as <strong>tack 'n' treads,</strong> are a <strong>great short-term solution to mark asphalt and pavements before permanent line marking takes place.</strong> They provide a way to delineate lanes and edges before the permanent longitudinal line marking process takes place.</p>

  <div class="details">
    <p>TRPMs or tack 'n' treads are available in <span class="hl">yellow or white and come with a Class 1A reflective strip</span> applied to tough high impact plastic. They are an <span class="hl">economical solution for making newly laid roads safer.</span></p>
    <p>An easy to remove clear cover protects the reflective film during sealing and is easily ripped off afterwards.</p>
  </div>

  <div class="price"><span class="price-tag">$0.40</span><span class="price-slash"></span><span class="price-note">ex GST per TRPM</span></div>

  <div class="dims-head"><span>Dimensions</span><i></i></div>
  <ul class="dims">
    <li>100 mm long x 50 mm high x 25 mm wide</li>
    <li>Double sided Class 1A Reflective</li>
    <li>Clear cover for reflective protection</li>
    <li>Available in all white, and red (reflective strip) and white, all yellow and all blue</li>
  </ul>

  <div class="range">
    <div class="range-item"><div class="r1" role="img" aria-label="Red, blue and yellow raised pavement markers"></div></div>
    <div class="range-item"><div class="r2" role="img" aria-label="Row of temporary pavement markers in white and yellow"></div></div>
    <div class="range-item"><div class="r3" role="img" aria-label="Bitumen adhesive pads for fixing markers"></div></div>
    <div class="range-item"><div class="r4" role="img" aria-label="Glow-in-the-dark reflective road studs"></div></div>
  </div>

  <svg class="call" viewBox="0 0 325 89" preserveAspectRatio="none" aria-hidden="true">
    <path d="M0 0 L250 0 C300 0 316 22 316 60 L316 89 L0 89 Z" fill="#f6c812"/>
    <path d="M0 0 L240 0 C288 0 306 22 306 60 L306 89 L0 89 Z" fill="#2460a7"/>
  </svg>
  <div class="call-text">
    <p class="lead">CALL TODAY</p>
    <p class="phone">02 9471 2385</p>
  </div>

  <p class="company">Kestrel Roadline Ventures Pty Ltd</p>
  <div class="web">www.krvlane.com</div>
  <div class="contact-bar">
    <span><svg width="14" height="10" viewBox="0 0 14 10" aria-hidden="true"><rect x="0.5" y="0.5" width="13" height="9" fill="none" stroke="#2460a7"/><path d="M0.5 0.5 L7 6 L13.5 0.5" fill="none" stroke="#2460a7"/></svg>marcus.t@krvsupply.com.au</span>
    <span><svg width="14" height="10" viewBox="0 0 14 10" aria-hidden="true"><rect x="0.5" y="0.5" width="13" height="9" fill="none" stroke="#2460a7"/><path d="M0.5 0.5 L7 6 L13.5 0.5" fill="none" stroke="#2460a7"/></svg>info@krvsupply.com.au</span>
  </div>
</main>
</body>
</html>
```